Postcard Design

We are a landscape maintenance, design and build company. Our services include weekly property maintenance, spring and fall clean ups, tree, shrub and plant care, pool renovations and new installations, patio and retaining wall design and construction, deign and building of outdoor kitchens, fireplaces and water features.we are a fully insured NJ Home Improvement Contractor License 27KP81926058

It Company

```html
<!DOCTYPE html>
<html lang="en">
<head>
<meta charset="utf-8">
<title>Birchline Contracting Postcard</title>
<link rel="stylesheet" href="https://fonts.googleapis.com/css2?family=Oswald:wght@500;600&family=Noto+Serif:wght@700&family=Lato:wght@400;700&display=swap">
<style>
  :root {
    --backdrop: #e7e3dd;
    --paper: #ffffff;
    --green: #109a47;
    --forest: #1c6b3a;
    --pine: #14502a;
    --mint: #47c979;
    --ink: #1a1a1a;
    --stamp: #8e8e8e;
    --photo-pool: #3d6db2;
    --photo-paver: #a7806a;
    --photo-stone: #7d8e98;
    --photo-brick: #b49783;
  }
  * { margin: 0; padding: 0; box-sizing: border-box; }
  html, body { width: 907px; height: 1200px; overflow: hidden; }
  body { background: var(--backdrop); position: relative; font-family: "Lato", sans-serif; }

  .card { position: absolute; left: 102px; width: 732px; background: var(--paper); overflow: hidden; }
  .card--front { top: 28px; height: 569px; }
  .card--back { top: 618px; height: 567px; }
  .card__shapes { position: absolute; inset: 0; }
  .card__text { position: absolute; white-space: nowrap; }

  .condensed { font-family: "Oswald", sans-serif; font-weight: 600; text-transform: uppercase; }
  .serif { font-family: "Noto Serif", serif; font-weight: 700; }

  /* Front brand block */
  .brand { position: absolute; left: 476px; top: 118px; width: 240px; text-align: center; }
  .brand__name { font-family: "Oswald", sans-serif; font-weight: 600; color: var(--ink); text-transform: uppercase; line-height: 1; }
  .brand__name--lead { font-size: 50px; letter-spacing: 1px; }
  .brand__name--tail { font-size: 25px; letter-spacing: 2px; margin-top: 4px; }
  .brand__tagline { font-family: "Noto Serif", serif; font-weight: 700; font-size: 13px; color: var(--ink); margin-top: 12px; }
  .brand__phone { font-family: "Noto Serif", serif; font-weight: 700; font-size: 19px; color: var(--ink); letter-spacing: 1px; }

  .headline-kicker { left: 18px; top: 412px; font-size: 17px; color: var(--forest); letter-spacing: 0.2px; }
  .headline-main { left: 18px; top: 436px; font-size: 28px; color: var(--ink); letter-spacing: 0.5px; }
  .license { left: 16px; top: 522px; font-size: 13px; color: var(--paper); }

  .cta { right: 22px; text-align: right; }
  .cta--label { top: 322px; font-size: 21px; color: var(--paper); letter-spacing: 0.5px; }
  .cta--phone { top: 350px; font-size: 30px; color: var(--mint); font-family: "Noto Serif", serif; font-weight: 400; }
  .cta--note { top: 398px; font-size: 17px; line-height: 24px; color: var(--paper); }

  /* Back */
  .services-tab { left: 86px; top: 152px; width: 217px; text-align: center; font-size: 19px; color: var(--paper); }
  .services { position: absolute; left: 30px; top: 201px; list-style: none; font-size: 15px; line-height: 19px; color: var(--ink); }
  .services__item { position: relative; padding-left: 18px; margin-bottom: 3px; }
  .services__item::before { content: ""; position: absolute; left: 2px; top: 5px; width: 9px; height: 9px; background: var(--forest); }

  .bar-label { left: 30px; top: 418px; font-size: 21px; color: var(--paper); }
  .bar-phone { left: 176px; top: 414px; font-size: 26px; color: var(--mint); font-family: "Noto Serif", serif; font-weight: 400; }

  .brand-mini { position: absolute; left: 430px; top: 44px; width: 96px; text-align: center; }
  .brand-mini__lead { font-family: "Oswald", sans-serif; font-weight: 600; font-size: 17px; line-height: 1; color: var(--ink); text-transform: uppercase; }
  .brand-mini__tail { font-family: "Oswald", sans-serif; font-weight: 600; font-size: 9px; line-height: 1; color: var(--ink); text-transform: uppercase; letter-spacing: 1px; margin-top: 2px; }
  .brand-mini__tagline { font-family: "Noto Serif", serif; font-weight: 700; font-size: 6px; color: var(--ink); margin-top: 3px; }
  .brand-mini__phone { font-family: "Noto Serif", serif; font-weight: 700; font-size: 8px; color: var(--ink); }
</style>
</head>
<body>

<section class="card card--front">
  <svg class="card__shapes" width="732" height="569" viewBox="0 0 732 569">
    <defs>
      <linearGradient id="patioPool" x1="0" y1="0" x2="0.3" y2="1">
        <stop offset="0" stop-color="var(--photo-pool)"/>
        <stop offset="0.3" stop-color="var(--photo-paver)"/>
        <stop offset="1" stop-color="#8c6a58"/>
      </linearGradient>
    </defs>
    <polygon points="0,0 546,0 350,317 0,317" fill="url(#patioPool)" role="img" aria-label="Photo of a paver patio with a circular inlay beside a swimming pool"/>
    <polygon points="556,0 572,0 378,317 362,317" fill="var(--green)"/>
    <polygon points="0,322 522,322 496,365 0,365" fill="var(--green)"/>
    <rect x="0" y="372" width="486" height="4" fill="var(--ink)"/>
    <polygon points="0,517 420,517 400,569 0,569" fill="var(--ink)"/>
    <polygon points="498,309 732,309 732,569 381,569" fill="var(--forest)"/>
    <rect x="412" y="478" width="290" height="91" fill="var(--pine)" role="img" aria-label="Row of pine tree silhouettes"/>
  </svg>

  <div class="brand">
    <div class="brand__name brand__name--lead">Birchline</div>
    <div class="brand__name brand__name--tail">Contracting</div>
    <div class="brand__tagline">Landscaping - Snow Removal</div>
    <div class="brand__phone">973-555-0192</div>
  </div>

  <p class="card__text serif headline-kicker">WE ARE A LANDSCAPE MAINTENANCE</p>
  <p class="card__text condensed headline-main">Design and Build Company</p>
  <p class="card__text license">License 27KP81926058</p>

  <p class="card__text condensed cta cta--label">Call Today</p>
  <p class="card__text cta cta--phone">0198765432</p>
  <p class="card__text condensed cta cta--note">We are a fully insured<br>NJ home improvement<br>contractor</p>
</section>

<section class="card card--back">
  <svg class="card__shapes" width="732" height="567" viewBox="0 0 732 567">
    <defs>
      <linearGradient id="stonePatio" x1="0" y1="0" x2="1" y2="1">
        <stop offset="0" stop-color="var(--photo-brick)"/>
        <stop offset="0.5" stop-color="var(--photo-stone)"/>
        <stop offset="1" stop-color="#9a8f86"/>
      </linearGradient>
    </defs>
    <polygon points="0,0 416,0 392,175 0,175" fill="url(#stonePatio)" role="img" aria-label="Photo of a bluestone patio with a round brick inlay"/>
    <polygon points="86,147 303,147 296,182 96,182" fill="var(--green)"/>
    <polygon points="420,0 431,0 352,460 341,460" fill="var(--green)"/>
    <polygon points="435,0 439,0 360,460 356,460" fill="var(--green)"/>
    <polygon points="0,407 145,407 175,460 0,460" fill="var(--ink)"/>
    <polygon points="145,407 346,407 338,460 175,460" fill="var(--forest)"/>
    <rect x="655" y="18" width="60" height="114" fill="var(--stamp)"/>
  </svg>

  <p class="card__text serif services-tab">Services</p>
  <ul class="services">
    <li class="services__item">weekly property maintenance</li>
    <li class="services__item">Spring and fall clean ups, tree, shrub</li>
    <li class="services__item">Plant care, pool renovations and<br>new installations</li>
    <li class="services__item">Patio and retaining wall design<br>and construction</li>
    <li class="services__item">Deign building of outdoor kitchens</li>
    <li class="services__item">Fireplaces and water features</li>
  </ul>

  <p class="card__text condensed bar-label">Call Today</p>
  <p class="card__text bar-phone">0198765432</p>

  <div class="brand-mini">
    <div class="brand-mini__lead">Birchline</div>
    <div class="brand-mini__tail">Contracting</div>
    <div class="brand-mini__tagline">Landscaping - Snow Removal</div>
    <div class="brand-mini__phone">973-555-0192</div>
  </div>
</section>

</body>
</html>
```